Vantor Advisory business card

Premium business card required
I have attached the brand as a powerpoint template but this can be made to look very up market, I have also attached my BIO for title reasons and to give you a feel for my skills
front of card
Derek Holloway
Managing Director Vantor Advisory
Retail, Customer-Led Experience, Transformation and Maximising Shareholder Return
Mobile +61(0)418557392
Email derekvantoradvisory.com
back of card

VANTOR ADVISORY’ OFFERING

We transform customer environments to extract benefits while elevating service levels;
We release millions of dollars in self-funding through continuous improvement;
We see CX as a key differentiator, proactively guarding share from market disrupters;
We re-invent service and create front-end of the future.

```html
<!DOCTYPE html>
<html lang="en">
<head>
<meta charset="utf-8">
<title>Vantor Advisory business card</title>
<link rel="stylesheet" href="https://fonts.googleapis.com/css2?family=Roboto:wght@400;700&family=Roboto+Condensed:wght@400;500&display=swap">
<style>
  :root {
    --backdrop: #2b2b2b;
    --slate-dark: #474747;
    --slate-light: #5e5e5e;
    --gold: #c8ae34;
    --disc: #ececec;
    --paper: #f1f1f1;
    --ink: #555555;
    --body-ink: #4a4a4a;
    --white: #ffffff;
  }
  * { margin: 0; padding: 0; box-sizing: border-box; }
  html, body { width: 1200px; height: 960px; overflow: hidden; }
  body {
    background: var(--backdrop);
    position: relative;
    font-family: "Roboto", Arial, sans-serif;
  }
  .card {
    position: absolute;
    width: 598px;
    height: 342px;
    overflow: hidden;
    box-shadow: 0 3px 8px rgba(0,0,0,.45);
  }
  /* Front */
  .card-front {
    left: 315px; top: 113px;
    background: linear-gradient(135deg, var(--slate-light), var(--slate-dark));
  }
  .front-art { position: absolute; inset: 0; }
  .holder-name {
    position: absolute; left: 38px; top: 42px;
    font-family: "Roboto Condensed", "Arial Narrow", sans-serif;
    font-weight: 500; font-size: 23px; color: var(--gold);
  }
  .holder-title {
    position: absolute; left: 38px; top: 71px;
    font-family: "Roboto Condensed", "Arial Narrow", sans-serif;
    font-size: 13px; line-height: 19.5px; color: var(--white);
  }
  .contact-list {
    position: absolute; left: 38px; top: 250px; list-style: none;
    font-size: 14.5px; color: var(--white);
  }
  .contact-list li { display: flex; align-items: center; height: 19.5px; }
  .contact-list svg { width: 12px; height: 12px; margin-right: 9px; fill: var(--gold); }
  .front-brand {
    position: absolute; left: 256px; top: 0; width: 342px; height: 342px;
    display: flex; align-items: center; justify-content: center; gap: 6px;
    padding-bottom: 24px;
  }
  .brand-word {
    font-family: "Roboto", Arial, sans-serif; font-weight: 700; color: var(--ink);
    line-height: 1;
  }
  .front-brand .brand-word { font-size: 34px; }
  .brand-dot { border-radius: 50%; background: var(--ink); flex: none; }
  .front-brand .brand-dot { width: 44px; height: 44px; }
  /* Back */
  .card-back { left: 311px; top: 472px; background: var(--paper); }
  .back-brand {
    position: absolute; left: 0; right: 0; top: 78px;
    display: flex; align-items: center; justify-content: center; gap: 14px;
  }
  .back-brand .brand-word { font-size: 60px; }
  .back-brand .brand-dot { width: 100px; height: 100px; }
  .offering-heading {
    position: absolute; left: 48px; right: 59px; top: 220px;
    display: flex; align-items: center; gap: 4px;
    font-family: "Roboto Condensed", "Arial Narrow", sans-serif;
    font-weight: 500; font-size: 20px; color: var(--gold); white-space: nowrap;
  }
  .offering-heading::before, .offering-heading::after {
    content: ""; flex: 1; height: 1px; background: #222;
  }
  .offering-list {
    position: absolute; left: 0; right: 0; top: 245px; list-style: none;
    text-align: center; font-size: 13px; line-height: 16px; color: var(--body-ink);
  }
</style>
</head>
<body>
  <section class="card card-front">
    <svg class="front-art" viewBox="0 0 598 342" aria-hidden="true">
      <defs>
        <filter id="disc-shadow" x="-10%" y="-10%" width="120%" height="120%">
          <feDropShadow dx="-2" dy="2" stdDeviation="3" flood-opacity=".35"/>
        </filter>
      </defs>
      <path d="M540 0 H598 V342 H452 Q560 250 540 0 Z" fill="var(--gold)"/>
      <circle cx="427" cy="171" r="171" fill="var(--disc)" filter="url(#disc-shadow)"/>
    </svg>
    <h1 class="holder-name">DEREK HOLLOWAY</h1>
    <p class="holder-title">Managing Director Vantor Advisory<br>Retail, Customer-Led Experience<br>Transformation &amp;<br>Maximising Shareholder Return</p>
    <ul class="contact-list">
      <li><svg viewBox="0 0 12 12"><rect x="3" y="0" width="6" height="12" rx="1"/></svg>+61(0)418557392</li>
      <li><svg viewBox="0 0 12 12"><path d="M0 2 H12 V10 H0 Z"/></svg>dh@derekvantoradvisory.com</li>
      <li><svg viewBox="0 0 12 12"><circle cx="6" cy="6" r="6"/></svg>derekvantoradvisory.com</li>
    </ul>
    <div class="front-brand">
      <span class="brand-word">KELDRAN</span><span class="brand-dot"></span>
    </div>
  </section>

  <section class="card card-back">
    <div class="back-brand">
      <span class="brand-word">KELDRAN</span><span class="brand-dot"></span>
    </div>
    <h2 class="offering-heading">VANTOR ADVISORY’ OFFERING</h2>
    <ul class="offering-list">
      <li>We transform customer environments to extract benefits while elevating service levels;</li>
      <li>We release millions of dollars in self-funding through continuous improvement;</li>
      <li>We see CX as a key differentiator, proactively guarding share from market disrupters;</li>
      <li>We re-invent service and create front-end of the future.</li>
    </ul>
  </section>
</body>
</html>
```